Corrigan & Hale, LLC
Business Cards & Stationery
Corrigan & Hale, LLC -
Creative Brief
Professional
Deborah L. Corrigan
Attorney At Law
418 W. Brookfield Avenue Suite 3B Pearl River, New York 10965-2274
dcorrigan@corriganandhale-example.com
www.corriganandhale-example.com
We will need to be able to use template for other people in the firm.
Specializing in Civil Litigation, Wills, Trusts & Estates, Guardianships, and related matters

```html
<!DOCTYPE html>
<html lang="en">
<head>
<meta charset="utf-8">
<title>Corrigan &amp; Hale, LLC — Business Card</title>
<link rel="stylesheet" href="https://fonts.googleapis.com/css2?family=Cinzel:wght@600&family=Libre+Baskerville:ital,wght@0,400;1,700&display=swap">
<style>
  :root {
    --backdrop: #e9e6e1;
    --card-white: #ffffff;
    --firm-green: #1d7a3b;
    --firm-green-deep: #0d4f22;
    --ink: #1f3a28;
    --swoosh-dark: #2b2b2b;
    --text-light: #ffffff;
    --rule: rgba(255,255,255,0.75);
  }
  html, body {
    margin: 0;
    width: 1200px;
    height: 780px;
    overflow: hidden;
    background: var(--backdrop);
  }
  .canvas {
    position: relative;
    width: 1200px;
    height: 780px;
  }
  .business-card {
    position: absolute;
    left: 75px;
    top: 90px;
    width: 1050px;
    height: 600px;
    border-radius: 34px;
    overflow: hidden;
    background: var(--card-white);
    box-shadow: 0 10px 30px rgba(0,0,0,0.18);
  }
  .card-bands {
    position: absolute;
    inset: 0;
  }
  .brand {
    position: absolute;
    left: 150px;
    top: 80px;
    display: flex;
    align-items: flex-start;
    gap: 34px;
  }
  .brand-mark {
    width: 92px;
    height: 92px;
    background: var(--firm-green);
    margin-top: 4px;
  }
  .brand-text {
    display: flex;
    flex-direction: column;
  }
  .firm-name {
    font-family: "Cinzel", serif;
    font-weight: 600;
    font-size: 50px;
    line-height: 1;
    color: var(--ink);
    letter-spacing: 1px;
    padding-bottom: 10px;
    border-bottom: 2px solid var(--ink);
  }
  .firm-tagline {
    font-family: "Cinzel", serif;
    font-weight: 600;
    font-size: 22px;
    color: var(--ink);
    letter-spacing: 3px;
    text-align: right;
    margin-top: 8px;
  }
  .contact-block {
    position: absolute;
    left: 0;
    right: 0;
    top: 385px;
    display: flex;
    color: var(--text-light);
    font-family: "Libre Baskerville", serif;
  }
  .person {
    width: 520px;
    text-align: right;
    padding-right: 30px;
    box-sizing: border-box;
  }
  .person-name {
    font-style: italic;
    font-weight: 700;
    font-size: 28px;
    margin: 0;
  }
  .person-title {
    font-size: 19px;
    margin: 6px 0 26px;
  }
  .person-address {
    font-size: 18px;
    line-height: 1.5;
    font-style: normal;
    margin: 0;
  }
  .divider {
    width: 2px;
    height: 160px;
    background: var(--rule);
  }
  .contact-list {
    list-style: none;
    margin: 0;
    padding: 0 0 0 26px;
    font-size: 18px;
  }
  .contact-list li {
    display: flex;
    align-items: center;
    gap: 12px;
    height: 32px;
  }
  .contact-icon {
    width: 20px;
    height: 20px;
    flex: none;
  }
</style>
</head>
<body>
<main class="canvas">
  <article class="business-card">
    <svg class="card-bands" viewBox="0 0 1050 600" preserveAspectRatio="none" aria-hidden="true">
      <defs>
        <linearGradient id="greenFill" x1="0" y1="0" x2="0" y2="1">
          <stop offset="0" stop-color="#23883f"/>
          <stop offset="1" stop-color="#0d4f22"/>
        </linearGradient>
        <linearGradient id="greyFill" x1="0" y1="0" x2="1" y2="0">
          <stop offset="0" stop-color="#d6d6d6"/>
          <stop offset="1" stop-color="#f2f2f2"/>
        </linearGradient>
      </defs>
      <path d="M0,285 C300,262 620,222 1050,175 L1050,230 C620,262 300,300 0,330 Z" fill="url(#greyFill)"/>
      <path d="M0,305 C300,290 620,250 1050,215 L1050,245 C620,272 300,312 0,340 Z" fill="var(--swoosh-dark)"/>
      <path d="M0,338 C300,312 620,272 1050,240 L1050,600 L0,600 Z" fill="url(#greenFill)"/>
    </svg>

    <header class="brand">
      <div class="brand-mark"></div>
      <div class="brand-text">
        <span class="firm-name">Corrigan &amp; Hale, LLC</span>
        <span class="firm-tagline">Attorneys at Law</span>
      </div>
    </header>

    <section class="contact-block">
      <div class="person">
        <h1 class="person-name">Deborah L. Corrigan</h1>
        <p class="person-title">Attorney At Law</p>
        <address class="person-address">418 W. Brookfield Avenue, Suite 3B<br>Ashford Falls, New York 10498-3317</address>
      </div>
      <div class="divider"></div>
      <ul class="contact-list">
        <li>
          <svg class="contact-icon" viewBox="0 0 20 20" aria-hidden="true"><path d="M5 2 L8 2 L9 6 L7 8 C8 11 9 12 12 13 L14 11 L18 12 L18 15 C18 17 16 18 14 18 C8 17 3 12 2 6 C2 4 3 2 5 2 Z" fill="#fff"/></svg>
          <span>212.555.0147</span>
        </li>
        <li>
          <svg class="contact-icon" viewBox="0 0 20 20" aria-hidden="true"><rect x="5" y="2" width="10" height="6" fill="#fff"/><rect x="2" y="8" width="16" height="8" rx="1.5" fill="#fff"/><rect x="5" y="13" width="10" height="5" fill="#fff"/></svg>
          <span>212.555.0193</span>
        </li>
        <li>
          <svg class="contact-icon" viewBox="0 0 20 20" aria-hidden="true"><circle cx="10" cy="10" r="8" fill="none" stroke="#fff" stroke-width="2.2"/><circle cx="10" cy="10" r="3" fill="none" stroke="#fff" stroke-width="2.2"/></svg>
          <span>dcorrigan@corriganandhale-example.com</span>
        </li>
        <li>
          <svg class="contact-icon" viewBox="0 0 20 20" aria-hidden="true"><circle cx="10" cy="10" r="8" fill="none" stroke="#fff" stroke-width="1.8"/><ellipse cx="10" cy="10" rx="3.5" ry="8" fill="none" stroke="#fff" stroke-width="1.5"/><line x1="2" y1="10" x2="18" y2="10" stroke="#fff" stroke-width="1.5"/></svg>
          <span>www.corriganandhale-example.com</span>
        </li>
      </ul>
    </section>
  </article>
</main>
</body>
</html>
```